PowerPoint Template for our Business

We are looking for a professional and visually appealing PowerPoint template for our business, Quorvane Labs. We specialize in calibration services and are currently undergoing a rebranding process. The new template should align with our updated brand identity, using the provided color palette and logos.
Project Requirements:
Title Slide:
Full Quorvane Labs logo prominently displayed.
Clean and professional layout.
Background color should be white with brand accents.
Title and subtitle areas clearly defined.
Content Slide:
Consistent use of brand colors for headers, footers, and other elements.
Space for text, images, charts, and graphs.
QL logo subtly incorporated.
Clean and modern layout ensuring readability and professionalism.
Section Header Slide:
Clear differentiation from content slides.
Use of QL logo and brand color for background.
Professional typography.
Closing Slide:
Full Quorvane Labs logo with a final message.
Clean background, professional layout.
Space for a thank you message and contact information.
Brand Colors:
Green: RGB (207, 255, 0)
Light Gray: RGB (239, 239, 239)
Gray: RGB (191, 191, 191)
Black: RGB (0, 0, 0)
White: RGB (255, 255, 255)
Deliverables:
A fully editable PowerPoint template (.pptx format).
Fonts and any additional assets used in the design.
Additional Information:
Please refer to the attached logos and color palette for guidance.
We are looking for a design that is not only professional and visually appealing but also functional for business presentations.
We look forward to seeing your creative proposals and selecting a design that best represents our brand.
Thank you!

```html
<!DOCTYPE html>
<html lang="en">
<head>
<meta charset="utf-8">
<title>Quorvane Labs – Presentation Template</title>
<link rel="stylesheet" href="https://fonts.googleapis.com/css2?family=Arimo:wght@400;700&display=swap">
<style>
:root{
  --green:#d4ff00;
  --black:#0a0a0a;
  --white:#ffffff;
  --light:#f5f5f5;
  --gray:#efefef;
  --mid:#bfbfbf;
  --stage:#4b4b4b;
  --text:#222222;
}
*{box-sizing:border-box;margin:0;padding:0}
html,body{width:1200px;height:4104px;overflow:hidden}
body{background:var(--stage);font-family:"Arimo",Helvetica,Arial,sans-serif;color:var(--text);position:relative}
.abs{position:absolute}
.slide{position:absolute;left:54px;width:1098px;height:617px;background:var(--white);overflow:hidden}
.header-band{position:absolute;left:0;top:0;width:1098px;height:84px}
.header-title{position:absolute;left:56px;top:22px;font-size:34px;color:var(--black);font-weight:400}
.header-title b{font-weight:700}
.header-mark{position:absolute;right:46px;top:24px;font-size:30px;font-weight:700;color:var(--green)}
.footer-date,.footer-page{position:absolute;top:572px;font-size:13px;font-weight:700;color:var(--black)}
.footer-date{left:56px}
.footer-page{right:56px}
.footer-bar{position:absolute;left:0;bottom:0;width:1098px;height:10px}
.body-text{position:absolute;font-size:13px;line-height:31.5px;text-align:justify;color:var(--text)}
.body-text p+p{margin-top:31.5px}
.watermark{position:absolute;font-size:360px;font-weight:700;color:#fbffe6;line-height:1}
.photo{position:absolute}

/* title slide */
.title-panel{position:absolute;left:27px;top:27px;width:616px;height:564px;background:var(--light)}
.brand-row{position:absolute;display:flex;align-items:center}
.brand-square{background:var(--black);flex:none}
.brand-name{color:var(--black);font-weight:400;white-space:nowrap}
.welcome{position:absolute;left:56px;top:250px;font-size:24px;color:var(--black)}
.welcome-title{position:absolute;left:56px;top:290px;font-size:54px;color:var(--black)}
.welcome-text{position:absolute;left:56px;top:352px;width:520px;font-size:13px;line-height:32px}
.social{position:absolute;top:441px;width:32px;height:32px;background:var(--black)}
.social::after{content:"";position:absolute;left:12px;top:12px;width:8px;height:8px;background:var(--green)}

/* chart */
.grid-line{position:absolute;left:129px;width:882px;height:1px;background:#e4e4e4}
.axis-label{position:absolute;left:40px;width:66px;text-align:right;font-size:16px;color:var(--black)}
.bar-track{position:absolute;top:234px;width:45px;height:258px;border-radius:10px;background:var(--gray);overflow:hidden}
.bar-fill{position:absolute;left:0;bottom:0;width:45px;border-radius:10px}
.bar-fill.dark{background:var(--black)}
.bar-fill.lime{background:var(--green)}
.year{position:absolute;top:505px;width:80px;margin-left:-17px;text-align:center;font-size:16px;color:var(--black)}

/* closing */
.contact-icon{position:absolute;width:50px;height:50px;border-radius:50%;background:var(--black)}
.contact-label{position:absolute;font-size:18px;font-weight:700;color:var(--black)}
.contact-value{position:absolute;font-size:18px;color:var(--black)}
.thanks-band{position:absolute;left:27px;top:502px;width:1051px;height:90px;background:var(--black);text-align:center;font-size:50px;line-height:90px;color:var(--green)}
.thanks-band b{font-weight:700}
</style>
</head>
<body>

<!-- Title slide -->
<section class="slide" style="top:48px">
  <div class="abs" style="left:0;top:261px;width:27px;height:356px;background:var(--green)"></div>
  <div class="abs" style="left:0;top:591px;width:643px;height:26px;background:var(--green)"></div>
  <div class="title-panel"></div>
  <div class="photo" role="img" aria-label="Close-up photograph of a precision measuring scale with a fine pointer" style="left:643px;top:27px;width:435px;height:564px;background:linear-gradient(135deg,#1c1c1c 0%,#3a3a3a 35%,#bdbdbd 60%,#8a8a8a 85%,#2a2a2a 100%)"></div>
  <div class="brand-row" style="left:56px;top:105px">
    <div class="brand-square" style="width:101px;height:101px"></div>
    <div class="brand-name" style="margin-left:30px;font-size:48px">Quorvane Labs</div>
  </div>
  <div class="welcome">WELCOME TO</div>
  <div class="welcome-title">Quorvane Labs</div>
  <div class="welcome-text">Itaque earum rerum hic tenetur a sapiente delectus, ut aut reiciendis voluptatibus maiores alias consequatur aut perferendis doloribus asperiores repellat.</div>
  <div class="social" style="left:57px"></div>
  <div class="social" style="left:110px"></div>
  <div class="social" style="left:161px"></div>
  <div class="social" style="left:212px"></div>
</section>

<!-- About slide -->
<section class="slide" style="top:727px">
  <svg class="header-band" viewBox="0 0 1098 84"><rect width="1098" height="84" fill="var(--black)"/><polygon points="0,0 894,0 929,84 0,84" fill="var(--green)"/></svg>
  <div class="header-title">About <b>Quorvane Labs</b></div>
  <div class="header-mark">QL</div>
  <div class="body-text" style="left:54px;top:145px;width:469px">
    <p>Nam libero tempore, cum soluta nobis est eligendi optio cumque nihil impedit quo minus id quod maxime placeat facere possimus, dignissimos ducimus qui blanditiis praesentium voluptatum deleniti praesentium voluptatum deleniti atque corrupti quos dolores et quas molestias praesentium voluptatum deleniti quos dolores et quas molestias sumenda est, omnis dolor repellendus.</p>
    <p>Temporibus autem quibusdam et aut officiis debitis aut rerum necessitatibus saepe eveniet ut et voluptates repudiandae sint et molestiae non recusandae. Itaque earum rerum hic tenetur a sapiente delectus, ut aut reiciendis voluptatibus maiores alias consequatur aut perferendis doloribus sapiente delectus asperiores repellat.</p>
  </div>
  <svg class="abs" style="left:595px;top:156px" width="490" height="334" viewBox="0 0 490 334"><polygon points="38,0 85,0 33,334 0,334" fill="var(--green)"/></svg>
  <div class="photo" role="img" aria-label="Photograph of gloved hands calibrating a micrometer" style="left:628px;top:156px;width:415px;height:334px;clip-path:polygon(10% 0,100% 0,100% 100%,0 100%);background:linear-gradient(160deg,#5a5f8a 0%,#9fb2dc 45%,#e3ebf8 70%,#6f86c0 100%)"></div>
  <div class="footer-date">14 May 2024</div>
  <div class="footer-page">Page No: 02</div>
  <svg class="footer-bar" viewBox="0 0 1098 10"><rect width="1098" height="10" fill="var(--green)"/><polygon points="0,0 815,0 825,10 0,10" fill="var(--black)"/></svg>
</section>

<!-- Why choose us -->
<section class="slide" style="top:1404px">
  <svg class="header-band" viewBox="0 0 1098 84"><rect width="1098" height="84" fill="var(--black)"/><polygon points="0,0 894,0 929,84 0,84" fill="var(--green)"/></svg>
  <div class="header-title">Why Choose <b>Us</b></div>
  <div class="header-mark">QL</div>
  <div class="watermark" style="left:540px;top:215px">QL</div>
  <div class="body-text" style="left:56px;top:146px;width:469px">
    <p>Nam libero tempore, cum soluta nobis est eligendi optio cumque nihil impedit quo minus id quod maxime placeat facere possimus, dignissimos ducimus qui blanditiis praesentium voluptatum deleniti praesentium voluptatum deleniti atque corrupti quos dolores et quas molestias praesentium voluptatum deleniti quos dolores et quas molestias sumenda est, omnis dolor repellendus.</p>
    <p>Temporibus autem quibusdam et aut officiis debitis aut rerum necessitatibus saepe eveniet ut et voluptates repudiandae sint et molestiae non recusandae. Itaque earum rerum hic tenetur a sapiente delectus, ut aut reiciendis voluptatibus maiores alias consequatur aut perferendis doloribus sapiente delectus asperiores repellat.</p>
  </div>
  <div class="body-text" style="left:576px;top:146px;width:470px">
    <p>Libero tempore, cum soluta nobis est eligendi optio cumque nihil impedit quo minus id quod maxime placeat facere possimus, dignissimos ducimus qui blanditiis praesentium voluptatum deleniti praesentium voluptatum deleniti atque corrupti quos dolores et quas molestias praesentium voluptatum deleniti quos dolores et quas molestias sumenda est, omnis dolor repellendus.</p>
    <p>Temporibus autem quibusdam et aut officiis debitis aut rerum necessitatibus saepe eveniet ut et voluptates repudiandae sint et molestiae non recusandae. Itaque earum rerum hic tenetur a sapiente delectus, ut aut reiciendis voluptatibus maiores alias consequatur aut perferendis doloribus sapiente delectus asperiores repellat.</p>
  </div>
  <div class="footer-date">14 May 2024</div>
  <div class="footer-page">Page No: 03</div>
  <svg class="footer-bar" viewBox="0 0 1098 10"><rect width="1098" height="10" fill="var(--green)"/><polygon points="0,0 815,0 825,10 0,10" fill="var(--black)"/></svg>
</section>

<!-- Graph -->
<section class="slide" style="top:2079px">
  <svg class="header-band" viewBox="0 0 1098 84"><rect width="1098" height="84" fill="var(--black)"/><polygon points="0,0 894,0 929,84 0,84" fill="var(--green)"/></svg>
  <div class="header-title">Our <b>Graph</b></div>
  <div class="header-mark">QL</div>
  <div class="body-text" style="left:58px;top:126px;width:990px;line-height:30px;text-align:left">Temporibus autem quibusdam et aut officiis debitis aut rerum necessitatibus saepe. Itaque earum rerum hic tenetur a sapiente delectus, ut aut reiciendis voluptatibus maiores alias consequatur aut perferendis doloribus asperiores repellat.</div>

  <div class="grid-line" style="top:236px"></div>
  <div class="grid-line" style="top:296px"></div>
  <div class="grid-line" style="top:356px"></div>
  <div class="grid-line" style="top:416px"></div>
  <div class="grid-line" style="top:476px"></div>
  <div class="axis-label" style="top:226px">100%</div>
  <div class="axis-label" style="top:286px">75%</div>
  <div class="axis-label" style="top:346px">50%</div>
  <div class="axis-label" style="top:405px">25%</div>
  <div class="axis-label" style="top:466px">0%</div>

  <div class="bar-track" style="left:168px"><div class="bar-fill dark" style="height:24%"></div></div>
  <div class="bar-track" style="left:260px"><div class="bar-fill lime" style="height:47%"></div></div>
  <div class="bar-track" style="left:351px"><div class="bar-fill dark" style="height:65%"></div></div>
  <div class="bar-track" style="left:447px"><div class="bar-fill lime" style="height:58%"></div></div>
  <div class="bar-track" style="left:538px"><div class="bar-fill dark" style="height:71%"></div></div>
  <div class="bar-track" style="left:630px"><div class="bar-fill lime" style="height:77%"></div></div>
  <div class="bar-track" style="left:723px"><div class="bar-fill dark" style="height:81%"></div></div>
  <div class="bar-track" style="left:820px"><div class="bar-fill lime" style="height:84%"></div></div>
  <div class="bar-track" style="left:911px"><div class="bar-fill dark" style="height:100%"></div></div>

  <div class="year" style="left:168px">2016</div>
  <div class="year" style="left:260px">2017</div>
  <div class="year" style="left:351px">2018</div>
  <div class="year" style="left:447px">2019</div>
  <div class="year" style="left:538px">2020</div>
  <div class="year" style="left:630px">2021</div>
  <div class="year" style="left:723px">2022</div>
  <div class="year" style="left:820px">2023</div>
  <div class="year" style="left:911px">2024</div>

  <div class="footer-date">14 May 2024</div>
  <div class="footer-page">Page No: 04</div>
  <svg class="footer-bar" viewBox="0 0 1098 10"><rect width="1098" height="10" fill="var(--green)"/><polygon points="0,0 815,0 825,10 0,10" fill="var(--black)"/></svg>
</section>

<!-- Chart -->
<section class="slide" style="top:2763px">
  <svg class="header-band" viewBox="0 0 1098 84"><rect width="1098" height="84" fill="var(--black)"/><polygon points="0,0 894,0 929,84 0,84" fill="var(--green)"/></svg>
  <div class="header-title">Our <b>Chart</b></div>
  <div class="header-mark">QL</div>
  <div class="watermark" style="left:540px;top:200px">QL</div>

  <svg class="abs" style="left:0;top:84px" width="580" height="430" viewBox="0 84 580 430" font-family="Arimo, Helvetica, Arial, sans-serif">
    <!-- pie depth -->
    <ellipse cx="289" cy="342" rx="104" ry="62" fill="#bdbdbd"/>
    <rect x="185" y="321" width="208" height="21" fill="#bdbdbd"/>
    <g transform="translate(289 321) scale(1 0.6)">
      <circle r="52" fill="none" stroke="#1f8fd6" stroke-width="104" stroke-dasharray="65.3 326.7" transform="rotate(-120)"/>
      <circle r="52" fill="none" stroke="#33b5ee" stroke-width="104" stroke-dasharray="84 326.7" transform="rotate(-48)"/>
      <circle r="52" fill="none" stroke="#7cc53a" stroke-width="104" stroke-dasharray="44.4 326.7" transform="rotate(44.6)"/>
      <circle r="52" fill="none" stroke="#f7921e" stroke-width="104" stroke-dasharray="60 326.7" transform="rotate(93.5)"/>
      <circle r="52" fill="none" stroke="#ececec" stroke-width="104" stroke-dasharray="73 326.7" transform="rotate(160)"/>
    </g>
    <!-- callout lines -->
    <g stroke="#9aa4ad" stroke-width="1" fill="none">
      <polyline points="172,242 210,242 240,285"/>
      <polyline points="390,246 360,250 330,280"/>
      <polyline points="418,330 380,330 370,340"/>
      <polyline points="374,350 340,370 330,350"/>
      <polyline points="160,318 200,318 215,330"/>
    </g>
    <!-- callout circles -->
    <g font-size="15" fill="#8a8a8a" text-anchor="middle">
      <circle cx="150" cy="242" r="21" fill="#fff" stroke="#e6e6e6" stroke-width="3"/><path d="M150 221 A21 21 0 0 1 170 248" stroke="#1f8fd6" stroke-width="3" fill="none"/><text x="150" y="247">20%</text>
      <circle cx="387" cy="223" r="21" fill="#fff" stroke="#e6e6e6" stroke-width="3"/><path d="M367 217 A21 21 0 0 1 406 216" stroke="#33b5ee" stroke-width="3" fill="none"/><text x="387" y="228">40%</text>
      <circle cx="446" cy="318" r="21" fill="#fff" stroke="#e6e6e6" stroke-width="3"/><path d="M430 305 A21 21 0 0 0 430 331" stroke="#7cc53a" stroke-width="3" fill="none"/><text x="446" y="323">17%</text>
      <circle cx="403" cy="427" r="21" fill="#fff" stroke="#e6e6e6" stroke-width="3"/><path d="M388 412 A21 21 0 0 0 392 445" stroke="#f7921e" stroke-width="3" fill="none"/><text x="403" y="432">23%</text>
      <circle cx="139" cy="398" r="21" fill="#fff" stroke="#e6e6e6" stroke-width="3"/><path d="M127 381 A21 21 0 0 0 125 413" stroke="#d0d0d0" stroke-width="3" fill="none"/><text x="139" y="403">25%</text>
    </g>
    <!-- callout labels -->
    <g font-size="6.5" fill="#777">
      <text x="76" y="227" font-weight="700">LOREM IPSUM</text>
      <text x="50" y="237">Brief note about this</text><text x="50" y="245">segment share</text>
      <text x="418" y="211" font-weight="700">LOREM IPSUM</text>
      <text x="418" y="221">Brief note about this</text><text x="418" y="229">segment share</text>
      <text x="478" y="307" font-weight="700">LOREM IPSUM</text>
      <text x="478" y="317">Brief note about this</text><text x="478" y="325">segment share</text>
      <text x="435" y="415" font-weight="700">LOREM IPSUM</text>
      <text x="435" y="425">Brief note about this</text><text x="435" y="433">segment share</text>
      <text x="65" y="386" font-weight="700">LOREM IPSUM</text>
      <text x="38" y="396">Brief note about this</text><text x="38" y="404">segment share</text>
    </g>
  </svg>

  <div class="body-text" style="left:574px;top:145px;width:523px;padding-right:0">
    <p style="width:469px">Libero tempore, cum soluta nobis est eligendi optio cumque nihil impedit quo minus id quod maxime placeat facere possimus, dignissimos ducimus qui blanditiis praesentium voluptatum deleniti praesentium voluptatum deleniti atque corrupti quos dolores et quas molestias praesentium voluptatum deleniti quos dolores et quas molestias sumenda est, omnis dolor repellendus.</p>
    <p style="width:469px">Temporibus autem quibusdam et aut officiis debitis aut rerum necessitatibus saepe eveniet ut et voluptates repudiandae sint et molestiae non recusandae. Itaque earum rerum hic tenetur a sapiente delectus, ut aut reiciendis voluptatibus maiores alias consequatur aut perferendis doloribus sapiente delectus asperiores repellat.</p>
  </div>
  <div class="footer-date">14 May 2024</div>
  <div class="footer-page">Page No: 05</div>
  <svg class="footer-bar" viewBox="0 0 1098 10"><rect width="1098" height="10" fill="var(--green)"/><polygon points="0,0 815,0 825,10 0,10" fill="var(--black)"/></svg>
</section>

<!-- Closing slide -->
<section class="slide" style="top:3438px">
  <div class="abs" style="left:0;top:0;width:643px;height:27px;background:var(--green)"></div>
  <div class="abs" style="left:0;top:0;width:27px;height:355px;background:var(--green)"></div>
  <div class="title-panel" style="width:1051px;height:475px"></div>
  <div class="brand-row" style="left:249px;top:117px">
    <div class="brand-square" style="width:128px;height:128px"></div>
    <div class="brand-name" style="margin-left:35px;font-size:60px">Quorvane Labs</div>
  </div>

  <div class="contact-icon" style="left:53px;top:318px">
    <svg width="50" height="50" viewBox="0 0 50 50"><path d="M25 15a7 7 0 0 0-7 7c0 5 7 13 7 13s7-8 7-13a7 7 0 0 0-7-7z" fill="var(--green)"/><circle cx="25" cy="22" r="2.6" fill="var(--black)"/></svg>
  </div>
  <div class="contact-label" style="left:117px;top:317px">LOCATION:</div>
  <div class="contact-value" style="left:117px;top:352px">Quorvane Labs, United States</div>

  <div class="contact-icon" style="left:439px;top:318px">
    <svg width="50" height="50" viewBox="0 0 50 50"><rect x="16" y="18" width="18" height="14" rx="1.5" fill="var(--green)"/><polyline points="16,19 25,26 34,19" fill="none" stroke="var(--black)" stroke-width="1.6"/></svg>
  </div>
  <div class="contact-label" style="left:501px;top:317px">EMAIL US:</div>
  <div class="contact-value" style="left:501px;top:352px">info@quorvanelabs.com</div>

  <div class="contact-icon" style="left:815px;top:318px">
    <svg width="50" height="50" viewBox="0 0 50 50"><path d="M19 15l4 0 2 6-3 2c1 3 3 5 6 6l2-3 6 2 0 4c0 1-1 2-2 2-10 0-17-7-17-17 0-1 1-2 2-2z" fill="var(--green)"/></svg>
  </div>
  <div class="contact-label" style="left:877px;top:317px">PHONE NUMBER:</div>
  <div class="contact-value" style="left:877px;top:357px">+1 555 014 2273</div>

  <div class="thanks-band">Thank <b>You</b></div>
</section>

</body>
</html>
```